HVAC company business card design

We need a business card design for a HVAC company. The design must look professional. Both sides will be used. The total data to be on the business card is
Name
Position
Email
Direct Phone/Moile Phone
Company Contacts /Address, Phone, Fax, web)
All data will be submit once the design is confirmed. For generic purposes use;
Emre Toksoy
Managing Director
+902324815263 (Mobile)
4712 Sokak No: 9 KBSE Yenikent IZMIR TURKEY
Tel: +902324815263 Fax : +902324815269
www.luvon.com.tr

Target Market(s)

HVAC

Industry/Entity Type

Business

Contact Information for Business Card

The total data to be on the business card is
Name
Position
Email
Direct Phone/Moile Phone
Emre Toksoy
Managing Director
+902324815263 (Mobile)
www.luvon.com.tr
The BC will use both sides of the card. The front will include the full logo and the details for the business card holder. The business card can be divided into vertical/horizontal or to a special shape. The common data like the company address/phone/fax should be indicated elsewehere. The back can contain some part or the whole logo and must contain the web address.

Font styles to use
Serif
Sans Serif

Colors
0355a3
cfdfed

Requirements
Should not have
• Please be careful with the fonts, it shouldnt be too small or too big and must not interfere with the logo fonts. If you need to use a curvy shape please do not use as the logo is already curvy or use the curves from the logo (if it looks good, otherwise forget it)
• We are not in favor of pictograms, only if they are perfect use them.

```html
<!DOCTYPE html>
<html lang="en">
<head>
<meta charset="utf-8">
<title>LUVON business card</title>
<link href="https://fonts.googleapis.com/css2?family=Source+Sans+3:wght@400;600&display=swap" rel="stylesheet">
<style>
  :root {
    --navy: #414b69;
    --navy-deep: #343c57;
    --brand-blue: #0355a3;
    --bright-blue: #2f6fd0;
    --pale-blue: #cfdfed;
    --silver: #a9aeb8;
    --white: #ffffff;
    --text-grey: #4a5063;
    --stage: #3a3a46;
  }
  * { margin: 0; padding: 0; box-sizing: border-box; }
  html, body { width: 1200px; height: 800px; overflow: hidden; }
  body {
    background: var(--stage);
    font-family: "Source Sans 3", sans-serif;
    display: flex;
    align-items: center;
    justify-content: center;
    gap: 40px;
  }
  .card {
    position: relative;
    width: 540px;
    height: 310px;
    overflow: hidden;
    border-radius: 3px;
    box-shadow: 0 10px 30px rgba(0,0,0,0.35);
  }
  .card-front { background: var(--white); }
  .card-back { background: linear-gradient(120deg, var(--navy-deep), var(--navy) 60%, #4a5474); }
  .wave { position: absolute; inset: 0; width: 100%; height: 100%; }

  .brand {
    position: absolute;
    display: flex;
    align-items: center;
    gap: 10px;
    color: var(--brand-blue);
    font-weight: 600;
    letter-spacing: 0.06em;
  }
  .card-front .brand { top: 26px; left: 26px; font-size: 40px; }
  .brand-dot {
    width: 44px; height: 44px;
    border-radius: 50%;
    background: var(--bright-blue);
  }

  .holder {
    position: absolute;
    right: 28px;
    top: 150px;
    text-align: right;
  }
  .holder-name { color: var(--bright-blue); font-size: 20px; font-weight: 600; }
  .holder-role { color: var(--text-grey); font-size: 13px; }

  .contacts {
    position: absolute;
    left: 26px;
    top: 150px;
    list-style: none;
    color: var(--white);
    font-size: 13px;
    line-height: 19px;
  }
  .contacts li { display: flex; align-items: center; gap: 8px; }
  .contacts svg { width: 11px; height: 11px; fill: var(--white); }

  .address {
    position: absolute;
    right: 28px;
    bottom: 24px;
    text-align: right;
    color: var(--white);
    font-size: 13px;
    line-height: 18px;
  }

  .card-back .brand {
    left: 150px;
    top: 110px;
    font-size: 78px;
    color: var(--white);
  }
  .card-back .brand-dot { width: 70px; height: 70px; }
  .back-web {
    position: absolute;
    right: 30px;
    bottom: 24px;
    color: var(--white);
    font-size: 14px;
  }
</style>
</head>
<body>

<section class="card card-front">
  <svg class="wave" viewBox="0 0 540 310" preserveAspectRatio="none" aria-hidden="true">
    <path d="M0,104 C140,72 250,86 330,160 C400,226 460,250 540,236 L540,310 L0,310 Z" fill="#b9bdc6"/>
    <path d="M0,112 C140,80 250,94 328,168 C398,234 460,256 540,244 L540,310 L0,310 Z" fill="var(--bright-blue)"/>
    <path d="M0,120 C140,88 248,102 324,176 C394,242 460,264 540,254 L540,310 L0,310 Z" fill="var(--navy)"/>
  </svg>

  <div class="brand"><span class="brand-dot"></span>LUVON</div>

  <div class="holder">
    <p class="holder-name">Emre Toksoy</p>
    <p class="holder-role">Managing Director</p>
  </div>

  <ul class="contacts">
    <li><svg viewBox="0 0 10 10"><rect x="2.5" y="0" width="5" height="10" rx="1"/></svg>+902324815263</li>
    <li><svg viewBox="0 0 10 10"><path d="M0,4 Q5,0 10,4 L8,5 L7,3.5 L3,3.5 L2,5 Z M2,6 H8 V10 H2 Z"/></svg>+902324815263</li>
    <li><svg viewBox="0 0 10 10"><rect x="0" y="4" width="10" height="6" rx="1"/><rect x="2" y="0" width="6" height="4"/></svg>+902324815269</li>
    <li><svg viewBox="0 0 10 10"><circle cx="5" cy="5" r="5"/></svg>www.luvon.com.tr</li>
  </ul>

  <div class="address">
    <p>4712 Sokak No: 9</p>
    <p>KBSE Yenikent IZMIR TURKEY</p>
  </div>
</section>

<section class="card card-back">
  <div class="brand"><span class="brand-dot"></span>LUVON</div>
  <p class="back-web">www.luvon.com.tr</p>
</section>

</body>
</html>
```